Stylish Design With Simple UI For Appointment Site

Note: Logo file now attached. Extra credit to anyone who offers basic HTML templates in the final deliverable, incorporating the individual components of the design (using DIVs and CSS).

There are two key requirements for this site:

1. It makes our site look like one of the most professional of its kind. We want to look the part;
2. It has a very simple, straight-forward user interface. We're nothing without being intuitive.

Our site will be used by other businesses to set up their own online booking systems.

Logo samples attached. The colour scheme is not yet set but two possible options are:

1. Dark (#323B3A) & Blue (#12B5D4) on White background
2. White & Yellow (#FEF102) on Grey (#3A3A3C) background

For inspiration, and an idea of what we like, take a look at quillbarn.com - it's very clear and eye-catching, although its pages are longer than we would like ours to be. Oh but we don't need a chimp! Instead of the section with the chimp in, we would like a changing image headline section on the home page, in the style of fellgarde.co.uk (with a less high image; we have attached one image which you may want to try out with this, but happy to see other ideas).

Any graphics included must be royalty free and free for commercial use. Fonts should be readily available and specified.

We would like to see the design applied to the following pages:

1. The main public home page (features header, login prompt, menu, changing image banner with headlines, main body, footer menu).
2. A secondary public page (features a similar layout to home page but without image headline banner, includes extra panels/body detail).
3. The Control Panel page (features several list panels and an add appointment button).
4. A list-style administration page (with popup item editor window).
5. A settings administration page (with form).

In that order, a sample walk-through design spec will be attached.

To summarise, we are looking for someone to put forward not only a design but something which also focuses on the user interface. The designer should consider all of the examples and guidance given, but shouldn't let that limit any innovation.

Happy to respond to any questions and give constant feedback.

Thank you.

-*-*-*-*-*-*-*-*-*-*-*-*-*-*-*-*-

Update, 18th Nov 2011:

1. I'm about the upload the logos so you can incorporate these into your designs.

2. A UI question of mine is how to move from a list view (e.g. Resources) to editing one of those items in the list. In the spec document I showed a popup editor for these items but I don't know if that's the best thing to do. Happy to see other ideas on this - whatever the best user experience would be.

3. On the designs in the spec document I've not included any help functionality. It would be good to include pieces of guidance on each page of the administration area to help the user - guess these could either be info panels on the pages themselves or info popups. Again, would be good to see some ideas in the designs.

Also, just to be clear, I am really looking for something that looks like a modern innovative "web app" rather than it looking like a promotional corporate web site.

Target Market(s)

Owners of businesses of all types (e.g. salons, small hotels, surgeries, etc).

Industry/Entity Type

Commercial

Requirements
Must have
• Headline image transition panel on home page.

Layout, graphic and font styles along similar lines to quillbarn.com, fellgarde.co.uk, etc.
Nice to have
• Blog feed panel on the home page.

Innovative ideas for improvements to the spec.
Should not have
• Anything which can't be practically rendered when the design is converted to HTML.

Should not be overly influenced by the layout and style in the attached spec - that should just be a guide to the content and layout of the site.

```html
<!DOCTYPE html>
<html lang="en">
<head>
<meta charset="utf-8">
<title>Slotwise – Control Panel</title>
<link rel="stylesheet" href="https://fonts.googleapis.com/css2?family=Roboto:wght@400;500;700&display=swap">
<style>
:root{
  --ink:#3a3a3c;
  --ink-dark:#2b2b2d;
  --black:#111;
  --yellow:#fed700;
  --yellow-hi:#ffe233;
  --paper:#f5f7f6;
  --card:#f7f8f8;
  --line:#c9cbcb;
  --text:#3a3a3a;
  --muted:#8a8a8a;
  --track:#e4e5e5;
  --thumb:#9a9c9c;
  --green:#33c133;
}
*{box-sizing:border-box;margin:0;padding:0}
html,body{width:1097px;height:1200px;overflow:hidden;background:var(--paper)}
body{font-family:"Roboto",Arial,sans-serif;color:var(--text)}
.stage{position:relative;width:1200px;height:1313px;transform:scale(.91417);transform-origin:0 0;background:var(--paper)}
.abs{position:absolute}

/* header */
.masthead{left:0;top:13px;width:1200px;height:237px;background:var(--ink)}
.page-top{left:0;top:0;width:1200px;height:13px;background:#fff}
.brand{left:110px;top:70px;display:flex;align-items:center;gap:14px;color:#fff;font-size:34px;font-weight:400;letter-spacing:6px}
.brand-mark{width:34px;height:34px;background:var(--yellow)}
.signout-tab{left:838px;top:0;width:254px;height:83px;background:linear-gradient(#ffe640,#fdc800);border-radius:0 0 4px 4px;box-shadow:0 2px 4px rgba(0,0,0,.35)}
.signout{left:910px;top:23px;width:106px;height:29px;background:var(--ink-dark);border-radius:4px;color:#fff;font-size:18px;font-weight:500;text-align:center;line-height:29px}

.nav{left:98px;top:191px;width:1002px;height:46px;background:var(--black);border-radius:0 3px 3px 0}
.nav-item{position:absolute;top:191px;height:46px;line-height:50px;color:#fff;font-size:24px;font-weight:700}
.nav-item.active{left:98px;top:182px;width:219px;height:55px;line-height:68px;background:linear-gradient(#ffe640,#fdc800);color:var(--ink-dark);text-align:center;border-radius:2px}

/* add button */
.add-btn{left:407px;top:276px;width:389px;height:54px;background:linear-gradient(#4a4a4c,#323234);border-radius:6px;color:#fff;font-size:26px;font-weight:700;display:flex;align-items:center}
.add-btn svg{margin:0 36px 0 25px}

/* filter bar */
.filter-bar{left:98px;top:354px;width:1002px;height:55px;background:linear-gradient(#454547,#303032);border-radius:7px;color:#fff;font-weight:700}
.filter-bar .t{position:absolute;top:0;line-height:58px;white-space:nowrap}
.fb-title{color:var(--yellow);font-size:22px}
.date-field{position:absolute;top:21px;width:83px;height:19px;background:#fff;border-radius:1px}
.resource-select{position:absolute;left:816px;top:21px;width:168px;height:19px;background:#fff;color:var(--text);font-weight:400;font-size:17px;line-height:19px;padding-left:39px}
.resource-select .box{position:absolute;left:8px;top:4px;width:17px;height:11px;border:2px solid var(--ink)}
.resource-select .drop{position:absolute;right:2px;top:2px;width:19px;height:15px;background:#fff;border:1px solid var(--ink)}

/* appointment cards */
.appt{left:98px;width:961px;height:103px;background:linear-gradient(#fdfdfd,#eff0f0);border:1px solid var(--line);border-radius:4px}
.appt .body{position:absolute;left:128px;top:8px;font-size:17px;line-height:21px}
.appt .when{font-weight:500}
.appt .res b{font-weight:500}
.appt .note{color:var(--muted);font-size:16px;line-height:20px;margin-top:4px;width:800px}

.cal{position:absolute;left:25px;top:11px;width:84px;height:80px;background:#fff;border:3px solid #d8d9d9;border-radius:9px;text-align:center;overflow:hidden}
.cal .mon{height:22px;background:var(--yellow);font-size:14px;font-weight:500;line-height:26px;color:var(--ink-dark)}
.cal .day{font-size:34px;font-weight:700;line-height:32px;color:var(--ink-dark)}
.cal .wd{font-size:13px;font-weight:500;line-height:14px;color:var(--ink-dark)}
.cal .ring{position:absolute;top:-2px;width:8px;height:20px;background:var(--ink);border-radius:4px}

/* scrollbars */
.scroll{width:30px;background:var(--track);border-radius:15px;overflow:hidden}
.scroll .cap{position:absolute;left:0;width:30px;height:32px;background:#9b9d9d;display:flex;align-items:center;justify-content:center}
.scroll .cap.up{top:0;border-radius:15px 15px 0 0}
.scroll .cap.down{bottom:0;border-radius:0 0 15px 15px}
.scroll .thumb{position:absolute;left:1px;width:28px;background:linear-gradient(90deg,#8f9191,#a9abab);border:1px solid #7d7f7f;border-radius:9px;display:flex;align-items:center;justify-content:center}

/* lower panels */
.panel-head{top:904px;width:480px;height:55px;background:linear-gradient(#454547,#2e2e30);border-radius:7px;color:var(--yellow);font-size:22px;font-weight:700;line-height:60px;padding-left:26px}
.pending{width:438px;height:70px;background:linear-gradient(#fdfdfd,#eff0f0);border:1px solid var(--line);border-radius:4px}
.pending .acts{position:absolute;left:35px;top:4px;display:flex;flex-direction:column;gap:6px}
.pending .body{position:absolute;left:85px;top:18px;font-size:17px;line-height:21px}
.pending .when{font-weight:500}
.pending .res b{font-weight:500}
.cancel-box{left:621px;top:979px;width:438px;height:230px;background:linear-gradient(#fafbfb,#f0f1f1);border:1px solid var(--line);border-radius:5px;padding:10px 24px;font-size:17px;font-weight:500}

/* footer */
.footer{left:0;top:1237px;width:1200px;height:76px;background:var(--ink);color:#fff;font-size:17px}
.footer .copy{position:absolute;left:99px;top:28px}
.footer .links{position:absolute;right:100px;top:27px;font-size:18px}
.footer .links span{margin:0 6px}
</style>
</head>
<body>
<div class="stage">

  <div class="abs page-top"></div>
  <header class="abs masthead"></header>
  <div class="abs brand"><span class="brand-mark"></span>SLOTWISE</div>
  <div class="abs signout-tab"></div>
  <div class="abs signout">SIGN OUT</div>

  <nav>
    <div class="abs nav"></div>
    <div class="nav-item active">CONTROL PANEL</div>
    <div class="nav-item" style="left:352px">RESOURCES</div>
    <div class="nav-item" style="left:544px">SERVICES &amp; EVENT</div>
    <div class="nav-item" style="left:813px">CLIENTS</div>
    <div class="nav-item" style="left:959px">SETTINGS</div>
  </nav>

  <div class="abs add-btn">
    <svg width="36" height="36" viewBox="0 0 36 36"><rect x="14" y="0" width="8" height="36" fill="#fed700"/><rect x="0" y="14" width="36" height="8" fill="#fed700"/></svg>
    Add New Appointment
  </div>

  <section class="abs filter-bar">
    <span class="t fb-title" style="left:23px">Upcoming Appointment</span>
    <svg class="abs" style="left:275px;top:20px" width="11" height="16" viewBox="0 0 11 16"><path d="M0 0L11 8L0 16Z" fill="#111"/></svg>
    <span class="t" style="left:302px;font-size:20px">Filter:</span>
    <span class="t" style="left:370px;font-size:17px">Start</span>
    <span class="date-field" style="left:421px"></span>
    <svg class="abs" style="left:514px;top:16px" width="22" height="24" viewBox="0 0 22 24"><rect x="1" y="4" width="20" height="19" rx="2" fill="#fff"/><rect x="1" y="4" width="20" height="7" fill="#fed700"/><rect x="5" y="1" width="3" height="6" fill="#555"/><rect x="14" y="1" width="3" height="6" fill="#555"/><text x="11" y="21" font-size="10" text-anchor="middle" fill="#333" font-family="Roboto,Arial,sans-serif">3</text></svg>
    <span class="t" style="left:547px;font-size:17px">End</span>
    <span class="date-field" style="left:596px"></span>
    <svg class="abs" style="left:689px;top:16px" width="22" height="24" viewBox="0 0 22 24"><rect x="1" y="4" width="20" height="19" rx="2" fill="#fff"/><rect x="1" y="4" width="20" height="7" fill="#fed700"/><rect x="5" y="1" width="3" height="6" fill="#555"/><rect x="14" y="1" width="3" height="6" fill="#555"/><text x="11" y="21" font-size="10" text-anchor="middle" fill="#333" font-family="Roboto,Arial,sans-serif">3</text></svg>
    <span class="abs" style="left:722px;top:10px;width:1px;height:36px;background:#777"></span>
    <span class="t" style="left:732px;font-size:17px">Resource</span>
    <div class="resource-select"><span class="box"></span>Bob Jones<span class="drop"><svg width="17" height="13" viewBox="0 0 17 13"><path d="M3 3H14L8.5 10Z" fill="#3a3a3c"/></svg></span></div>
  </section>

  <!-- upcoming appointments -->
  <article class="abs appt" style="top:424px">
    <div class="cal"><span class="ring" style="left:11px"></span><span class="ring" style="right:11px"></span><div class="mon">OCT</div><div class="day">3</div><div class="wd">Monday</div></div>
    <div class="body"><div class="when">Mon, Oct 3, 2011, 20:00 – 23:45</div><div class="res"><b>Recourses:</b> Bob Jones, Treatmen Chair 1</div><div class="note">Many desktop publishing packages and web page editors now use Lorem Ipsum as their default model text, and a search for 'lorem ipsum' will uncover many web sites still in their infancy.....</div></div>
  </article>
  <article class="abs appt" style="top:543px">
    <div class="cal"><span class="ring" style="left:11px"></span><span class="ring" style="right:11px"></span><div class="mon">AUG</div><div class="day">16</div><div class="wd">Thursday</div></div>
    <div class="body"><div class="when">Thu, Aug 16, 2011, 07:00 – 09:00</div><div class="res"><b>Recourses:</b> Bob Jones, Treatmen Chair 1</div><div class="note">Many desktop publishing packages and web page editors now use Lorem Ipsum as their default model text, and a search for 'lorem ipsum' will uncover many web sites still in their infancy.....</div></div>
  </article>
  <article class="abs appt" style="top:659px">
    <div class="cal"><span class="ring" style="left:11px"></span><span class="ring" style="right:11px"></span><div class="mon">AUG</div><div class="day">27</div><div class="wd">Monday</div></div>
    <div class="body"><div class="when">Mon, Aug 27, 2011, 20:00 – 23:45</div><div class="res"><b>Recourses:</b> Sian Oven, Treatmen Chair 1</div><div class="note">Many desktop publishing packages and web page editors now use Lorem Ipsum as their default model text, and a search for 'lorem ipsum' will uncover many web sites still in their infancy.....</div></div>
  </article>
  <article class="abs appt" style="top:779px">
    <div class="cal"><span class="ring" style="left:11px"></span><span class="ring" style="right:11px"></span><div class="mon">JULY</div><div class="day">31</div><div class="wd">Sunday</div></div>
    <div class="body"><div class="when">Mon, Oct 3, 2011, 20:00 – 23:45</div><div class="res"><b>Recourses:</b> Sian Oven, Treatmen Chair 1</div><div class="note">Many desktop publishing packages and web page editors now use Lorem Ipsum as their default model text, and a search for 'lorem ipsum' will uncover many web sites still in their infancy.....</div></div>
  </article>

  <div class="abs scroll" style="left:1070px;top:424px;height:458px">
    <div class="cap up"><svg width="16" height="10"><path d="M8 0L16 10H0Z" fill="#1e1e1e"/></svg></div>
    <div class="thumb" style="top:170px;height:116px"><svg width="18" height="14"><path d="M0 2H18M0 7H18M0 12H18" stroke="#e8e8e8" stroke-width="2"/></svg></div>
    <div class="cap down"><svg width="16" height="10"><path d="M0 0H16L8 10Z" fill="#1e1e1e"/></svg></div>
  </div>

  <!-- awaiting confirmation -->
  <div class="abs panel-head" style="left:98px">Appointment Awaiting Confirmation</div>
  <article class="abs pending" style="left:99px;top:979px">
    <div class="acts">
      <svg width="32" height="27"><rect width="32" height="27" rx="3" fill="#333"/><path d="M6 14L13 21L27 4" stroke="#33c133" stroke-width="5" fill="none"/></svg>
      <svg width="32" height="27"><rect width="32" height="27" rx="3" fill="#333"/><path d="M9 6L23 21M23 6L9 21" stroke="#fed700" stroke-width="4"/></svg>
    </div>
    <div class="body"><div class="when">Mon, Oct 3, 2011, 20:00 – 23:45</div><div class="res"><b>Recourses:</b> Bob Jones, Treatmen Chair 1</div></div>
  </article>
  <article class="abs pending" style="left:99px;top:1058px;width:437px">
    <div class="acts">
      <svg width="32" height="27"><rect width="32" height="27" rx="3" fill="#333"/><path d="M6 14L13 21L27 4" stroke="#33c133" stroke-width="5" fill="none"/></svg>
      <svg width="32" height="27"><rect width="32" height="27" rx="3" fill="#333"/><path d="M9 6L23 21M23 6L9 21" stroke="#fed700" stroke-width="4"/></svg>
    </div>
    <div class="body"><div class="when">Thu, Aug 16, 2011, 07:00 – 09:00</div><div class="res"><b>Recourses:</b> Bob Jones, Treatmen Chair 1</div></div>
  </article>
  <article class="abs pending" style="left:97px;top:1139px">
    <div class="acts">
      <svg width="32" height="27"><rect width="32" height="27" rx="3" fill="#333"/><path d="M6 14L13 21L27 4" stroke="#33c133" stroke-width="5" fill="none"/></svg>
      <svg width="32" height="27"><rect width="32" height="27" rx="3" fill="#333"/><path d="M9 6L23 21M23 6L9 21" stroke="#fed700" stroke-width="4"/></svg>
    </div>
    <div class="body"><div class="when">Mon, Oct 3, 2011, 20:00 – 23:45</div><div class="res"><b>Recourses:</b> Sian Oven, Treatmen Chair 1</div></div>
  </article>
  <div class="abs scroll" style="left:549px;top:977px;height:234px">
    <div class="cap up"><svg width="16" height="10"><path d="M8 0L16 10H0Z" fill="#1e1e1e"/></svg></div>
    <div class="thumb" style="left:3px;width:24px;top:89px;height:42px"><svg width="16" height="14"><path d="M0 2H16M0 7H16M0 12H16" stroke="#e8e8e8" stroke-width="2"/></svg></div>
    <div class="cap down"><svg width="16" height="10"><path d="M0 0H16L8 10Z" fill="#1e1e1e"/></svg></div>
  </div>

  <!-- cancellations -->
  <div class="abs panel-head" style="left:621px;width:479px">Recent Cancellations</div>
  <div class="abs cancel-box">No Recent Cancellations</div>
  <div class="abs scroll" style="left:1070px;top:977px;height:234px">
    <div class="cap up"><svg width="16" height="10"><path d="M8 0L16 10H0Z" fill="#1e1e1e"/></svg></div>
    <div class="thumb" style="left:3px;width:24px;top:89px;height:42px"><svg width="16" height="14"><path d="M0 2H16M0 7H16M0 12H16" stroke="#e8e8e8" stroke-width="2"/></svg></div>
    <div class="cap down"><svg width="16" height="10"><path d="M0 0H16L8 10Z" fill="#1e1e1e"/></svg></div>
  </div>

  <footer class="abs footer">
    <div class="copy">Copyright © 2011 Slotwise. All Rights Reserved</div>
    <div class="links">HOME<span>|</span>FEATURES<span>|</span>PRICING<span>|</span>CONTACT US</div>
  </footer>

</div>
</body>
</html>
```